Business Card Design

Please see my website www.qvloreming.com.au to for further information on my services and styling of my site

Reason: Deadline is extended to permit alterations to current designs or for any new submissions. Cheers

Industry/Entity Type

Business

Contact Information for Business Card

Marcus Thorne
Empowerment Coach

'Live your passion'

marcus@qvtraining.com.au
0437158204
qvtraining.com.au

```html
<!DOCTYPE html>
<html lang="en">
<head>
<meta charset="utf-8">
<title>QVT Business Card</title>
<link rel="stylesheet" href="https://fonts.googleapis.com/css2?family=Arimo:wght@400;700&display=swap">
<style>
  :root {
    --bg: #dcdcdc;
    --green: #97c93d;
    --green-dark: #86b832;
    --white: #ffffff;
    --ink: #3a3a3a;
    --ghost-light: #ececec;
    --ghost-green: #8ab936;
  }
  * { box-sizing: border-box; margin: 0; padding: 0; }
  html, body { width: 1200px; height: 985px; overflow: hidden; }
  body {
    background: var(--bg);
    font-family: "Arimo", Arial, sans-serif;
    position: relative;
  }
  .card {
    position: absolute;
    left: 280px;
    width: 640px;
    height: 390px;
    border-radius: 26px;
    overflow: hidden;
  }
  .card-back { top: 75px; background: var(--white); }
  .card-front { top: 520px; background: var(--green); }

  .silhouette-area {
    position: absolute;
    border-radius: 40px;
  }
  .card-back .silhouette-area {
    left: 60px; top: 30px; width: 340px; height: 270px;
    background: radial-gradient(ellipse at 40% 50%, var(--ghost-light) 0%, rgba(236,236,236,0) 72%);
  }
  .card-front .silhouette-area {
    left: 170px; top: 60px; width: 330px; height: 300px;
    background: radial-gradient(ellipse at 45% 55%, var(--ghost-green) 0%, rgba(138,185,54,0) 72%);
  }

  .brand {
    position: absolute;
    right: 48px;
    display: flex;
    align-items: center;
    gap: 14px;
  }
  .brand-text { display: flex; flex-direction: column; align-items: flex-start; }
  .brand-name {
    font-size: 46px;
    font-weight: 700;
    letter-spacing: 2px;
    line-height: 1;
  }
  .brand-tagline {
    font-size: 14px;
    font-weight: 700;
    letter-spacing: 0.5px;
    margin-top: 6px;
    padding-top: 5px;
    border-top: 2px solid currentColor;
  }
  .brand-dot { width: 34px; height: 34px; border-radius: 50%; }

  .card-back .brand { bottom: 102px; }
  .card-back .brand-name { color: var(--green); }
  .card-back .brand-tagline { color: var(--ink); }
  .card-back .brand-dot { background: var(--ink); }

  .web-band {
    position: absolute;
    left: 0; bottom: 0;
    width: 360px; height: 54px;
    background: var(--green);
    border-top-right-radius: 26px;
    display: flex;
    align-items: center;
    padding-left: 26px;
    gap: 18px;
    color: var(--white);
    font-size: 20px;
  }
  .web-band .icon-badge {
    width: 26px; height: 26px; border-radius: 50%;
    background: var(--white);
    display: flex; align-items: center; justify-content: center;
  }

  .identity {
    position: absolute;
    left: 46px; top: 30px;
    color: var(--white);
  }
  .identity .name { font-size: 26px; }
  .identity .role {
    font-size: 19px;
    margin-top: 6px;
    padding-bottom: 8px;
    border-bottom: 1.5px solid var(--white);
    width: 230px;
  }

  .contact-tab {
    position: absolute;
    left: 0; top: 132px;
    width: 34px; height: 104px;
    background: var(--white);
    border-radius: 0 14px 14px 0;
    display: flex; flex-direction: column;
    align-items: center; justify-content: space-around;
    padding: 6px 0;
  }
  .contact-icon {
    width: 20px; height: 20px; border-radius: 5px;
    background: var(--green);
    display: flex; align-items: center; justify-content: center;
  }
  .contact-list {
    position: absolute;
    left: 46px; top: 134px;
    list-style: none;
    color: var(--white);
    font-size: 20px;
    line-height: 34px;
  }

  .card-front .brand { bottom: 52px; }
  .card-front .brand-name,
  .card-front .brand-tagline { color: var(--white); }
  .card-front .brand-dot { background: var(--white); }
</style>
</head>
<body>

  <section class="card card-back" aria-label="Card back">
    <div class="silhouette-area" role="img" aria-label="Faint silhouettes of people with raised arms"></div>
    <div class="brand">
      <div class="brand-text">
        <span class="brand-name">QVT</span>
        <span class="brand-tagline">Quest Vitality Training</span>
      </div>
      <span class="brand-dot"></span>
    </div>
    <div class="web-band">
      <span class="icon-badge">
        <svg width="18" height="18" viewBox="0 0 24 24" fill="none" stroke="#97c93d" stroke-width="2">
          <circle cx="12" cy="12" r="9"/><path d="M3 12h18M12 3c3 3 3 15 0 18M12 3c-3 3-3 15 0 18"/>
        </svg>
      </span>
      <span class="web-address">www.qvbalance.com.au</span>
    </div>
  </section>

  <section class="card card-front" aria-label="Card front">
    <div class="silhouette-area" role="img" aria-label="Faint silhouettes of people with raised arms"></div>
    <div class="identity">
      <p class="name">Marcus Thorne</p>
      <p class="role">Empowerment Coach</p>
    </div>
    <div class="contact-tab">
      <span class="contact-icon">
        <svg width="12" height="12" viewBox="0 0 24 24" fill="#fff"><path d="M6.6 10.8a15 15 0 0 0 6.6 6.6l2.2-2.2a1 1 0 0 1 1-.25 11.4 11.4 0 0 0 3.6.6 1 1 0 0 1 1 1V20a1 1 0 0 1-1 1A17 17 0 0 1 3 4a1 1 0 0 1 1-1h3.5a1 1 0 0 1 1 1c0 1.25.2 2.45.6 3.6a1 1 0 0 1-.25 1z"/></svg>
      </span>
      <span class="contact-icon">
        <svg width="13" height="13" viewBox="0 0 24 24" fill="none" stroke="#fff" stroke-width="2.4"><circle cx="12" cy="12" r="9"/><path d="M3 12h18M12 3c3 3 3 15 0 18M12 3c-3 3-3 15 0 18"/></svg>
      </span>
      <span class="contact-icon">
        <svg width="13" height="13" viewBox="0 0 24 24" fill="none" stroke="#fff" stroke-width="2.4"><rect x="3" y="5" width="18" height="14" rx="1"/><path d="M3 6l9 7 9-7"/></svg>
      </span>
    </div>
    <ul class="contact-list">
      <li>0437158204</li>
      <li>qvtraining.com.au</li>
      <li>marcus@qvtraining.com.au</li>
    </ul>
    <div class="brand">
      <div class="brand-text">
        <span class="brand-name">QVT</span>
        <span class="brand-tagline">Quest Vitality Training</span>
      </div>
      <span class="brand-dot"></span>
    </div>
  </section>

</body>
</html>
```